Business Card for Bright Meadow Lawn & Landscape

Double Sided Card Design - I think one side of the card should be cleaner, with logo, contact info, and "Complete Residential & Commercial Landscape Services", and on the other side it should list the services we offer:

- Lawn Care & Mowing
- Hedge & Shrub Trimming
- Leaf Removal & Clean Up
- Aeration & Sod
- Mulch & Rock Installations
- Landscape Installations & Renovations
- Commercial Snow Removal

Please make it clean and very professional... don't want it too be too busy, but want to tell them what we do.

Target Market(s)

Residential and Commercial

Industry/Entity Type

Landscape

Contact Information for Business Card

Fully Insured
Tom Berrigan
410-555-0198
Tberrigan07@mailbox-example.com

Requirements
Must have
• Double Sided, Cleaner on one side, more information and text on the other side.

```html
<!DOCTYPE html>
<html lang="en">
<head>
<meta charset="utf-8">
<title>Bright Meadow Lawn &amp; Landscape – Business Card</title>
<link href="https://fonts.googleapis.com/css2?family=Open+Sans:wght@400;600;700&display=swap" rel="stylesheet">
<style>
  :root {
    --bg: #2a2c2f;
    --card-dark: #222629;
    --panel-gray: #3a3e42;
    --circle-dark: #1f2225;
    --green: #7cb843;
    --green-text: #8cc63f;
    --white: #ffffff;
  }
  * { box-sizing: border-box; margin: 0; padding: 0; }
  html, body { width: 1200px; height: 959px; overflow: hidden; }
  body {
    background: var(--bg);
    font-family: "Open Sans", Arial, sans-serif;
    position: relative;
  }
  .card {
    position: absolute;
    left: 220px;
    width: 760px;
    height: 434px;
    border-radius: 4px;
    overflow: hidden;
    box-shadow: 0 14px 30px rgba(0,0,0,0.45);
  }
  /* Back side: services */
  .card-back { top: 30px; background: var(--card-dark); }
  .card-back .accent-stripe {
    position: absolute; left: 0; top: 0; bottom: 0; width: 24px;
    background: var(--green);
  }
  .card-back .faint-ring { position: absolute; right: -40px; top: -30px; }
  .services {
    position: absolute; left: 70px; top: 120px;
    color: var(--green-text);
  }
  .services-title {
    font-weight: 700; font-size: 20px; letter-spacing: 0.5px;
    margin-bottom: 18px;
  }
  .services-list { list-style: none; font-size: 19px; line-height: 31px; }
  .services-list li::before { content: "• "; }

  /* Front side: contact */
  .card-front { top: 495px; background: var(--green); }
  .card-front .panel { position: absolute; inset: 0; }
  .brand {
    position: absolute; left: 60px; top: 40px;
    display: flex; align-items: center; gap: 12px;
    color: var(--white);
  }
  .brand-dot { width: 34px; height: 34px; border-radius: 50%; background: var(--white); }
  .brand-name { font-weight: 600; font-size: 17px; line-height: 21px; }
  .contact { position: absolute; left: 60px; top: 140px; color: var(--white); }
  .insured { font-size: 22px; font-weight: 400; letter-spacing: 0.5px; margin-bottom: 18px; }
  .person { font-size: 34px; font-weight: 400; margin-bottom: 8px; }
  .line { display: flex; align-items: center; gap: 12px; font-size: 19px; line-height: 32px; }
  .line svg { flex: none; }
  .tagline { margin-top: 30px; font-size: 14px; line-height: 20px; max-width: 240px; }
</style>
</head>
<body>

<section class="card card-back" aria-label="Card back – services">
  <div class="accent-stripe"></div>
  <svg class="faint-ring" width="420" height="420" viewBox="0 0 420 420" aria-hidden="true">
    <circle cx="210" cy="210" r="180" fill="none" stroke="#2b3030" stroke-width="40"/>
  </svg>
  <div class="services">
    <h2 class="services-title">SERVICES WE OFFER:</h2>
    <ul class="services-list">
      <li>Lawn Care &amp; Mowing</li>
      <li>Hedge &amp; Shrub Trimming</li>
      <li>Leaf Removal &amp; Clean Up</li>
      <li>Aeration &amp; Sod</li>
      <li>Mulch &amp; Rock Installations</li>
      <li>Landscape Installations &amp; Renovations</li>
      <li>Commercial Snow Removal</li>
    </ul>
  </div>
</section>

<section class="card card-front" aria-label="Card front – contact">
  <svg class="panel" width="760" height="434" viewBox="0 0 760 434" aria-hidden="true">
    <path d="M470 0 H760 V434 H610 C700 330 720 120 470 0 Z" fill="var(--panel-gray)"/>
    <circle cx="560" cy="215" r="170" fill="var(--circle-dark)"/>
  </svg>
  <div class="brand">
    <span class="brand-dot"></span>
    <span class="brand-name">Bright Meadow<br>Lawn &amp; Landscape</span>
  </div>
  <div class="contact">
    <p class="insured">FULLY INSURED</p>
    <p class="person">Tom Berrigan</p>
    <p class="line">
      <svg width="20" height="20" viewBox="0 0 20 20" aria-hidden="true"><circle cx="10" cy="10" r="10" fill="#fff"/><path d="M7 5.5l2 2-1 1.2c.6 1.3 1.6 2.3 2.8 2.8l1.2-1 2 2-1.2 1.5C9.5 13.8 6.2 10.5 5.5 7z" fill="var(--green)"/></svg>
      410-555-0198
    </p>
    <p class="line">
      <svg width="20" height="20" viewBox="0 0 20 20" aria-hidden="true"><circle cx="10" cy="10" r="10" fill="#fff"/><rect x="5" y="6.5" width="10" height="7" fill="none" stroke="var(--green)" stroke-width="1.4"/><path d="M5 6.5l5 4 5-4" fill="none" stroke="var(--green)" stroke-width="1.4"/></svg>
      Tberrigan07@mailbox-example.com
    </p>
    <p class="tagline">Complete Residential &amp; Commercial Landscape Services</p>
  </div>
</section>

</body>
</html>
```